We need a podcast cover design that will be used on Vellora. The podcast is called Founder Temperament Signal. The people we want to attract want us to be direct, real and upfront wiht them. They live in a noisy world and want clear and elegant design and funciton. We work with entrepreneurs who like brands like Quince, Brivo and Marlo. We want a simple elegant design that uses the title on the cover along with the photo we uploaded. If someone goes to vellora, we want this to stand out and be visible.

Target Market(s)

Entrepreneurs, Artists, People who think differently

Industry/Entity Type

Consultant

Font styles to use
Sans Serif

Colors

Designer to choose colors to be used in the design.

Requirements
Must have
• The title on the podcast cover that will be legible on Vellora. There should be high contrast so that the cover stands out on vellora with everyoe else.
Nice to have
• I would like to see the photo offset either right or left and bleeding off the page.
Should not have
• Too many colors, patterns or designs. Simple, elegant, and clean.

```html
<!DOCTYPE html>
<html lang="en">
<head>
<meta charset="utf-8">
<title>Founder Temperament Signal — Podcast Cover</title>
<link rel="stylesheet" href="https://fonts.googleapis.com/css2?family=Montserrat:wght@300;900&display=swap">
<style>
  :root {
    --slate: #58595b;
    --paper: #ffffff;
    --title-white: #ffffff;
    --amber: #f0ab1a;
    --photo-top: #e6b394;
    --photo-mid: #c98f6c;
    --photo-bottom: #8cc6dc;
  }
  html, body {
    margin: 0;
    padding: 0;
    width: 1200px;
    height: 1200px;
    overflow: hidden;
    background: var(--paper);
  }
  .cover {
    position: relative;
    width: 1200px;
    height: 1200px;
    background: var(--paper);
    overflow: hidden;
  }
  .title-column {
    position: absolute;
    left: 0;
    top: 0;
    width: 503px;
    height: 1200px;
    background: var(--slate);
  }
  .host-photo {
    position: absolute;
    left: 840px;
    top: 0;
    width: 360px;
    height: 1200px;
    background: linear-gradient(180deg, var(--photo-top) 0%, var(--photo-mid) 78%, var(--photo-bottom) 92%, var(--photo-bottom) 100%);
  }
  .title-main {
    position: absolute;
    left: 74px;
    top: 0;
    margin: 0;
    font-family: "Montserrat", sans-serif;
    font-weight: 900;
    font-size: 184px;
    letter-spacing: -7px;
    color: var(--title-white);
    text-transform: uppercase;
  }
  .title-main span,
  .title-sub span {
    position: absolute;
    left: 0;
    white-space: nowrap;
    line-height: 1;
  }
  .title-main .l1 { top: 64px; }
  .title-main .l2 { top: 228px; }
  .title-main .l3 { top: 392px; }
  .title-sub {
    position: absolute;
    left: 72px;
    top: 0;
    margin: 0;
    font-family: "Montserrat", sans-serif;
    font-weight: 300;
    font-size: 100px;
    letter-spacing: -3px;
    color: var(--amber);
    text-transform: uppercase;
  }
  .title-sub .s1 { top: 911px; }
  .title-sub .s2 { top: 1021px; }
</style>
</head>
<body>
  <main class="cover">
    <div class="title-column"></div>

    <div class="host-photo" role="img" aria-label="Photo of the smiling host, cropped to half his face and bleeding off the right edge"></div>

    <h1 class="title-main" aria-label="Founder">
      <span class="l1">FOU</span>
      <span class="l2">NDE</span>
      <span class="l3">R</span>
    </h1>
    <p class="title-sub">
      <span class="s1">Temperament</span>
      <span class="s2">Signal</span>
    </p>
  </main>
</body>
</html>
```